Pop up exhibition stand 2000mm (H) x 800mm (W)

I would like a simple pop up banner stand for an exhibition.

We need a pop up banner stand design for 'Brindle Forge Services'

the size is 2000mm(H) x 800mm (W)

Ad copy as follows :

[Brindle Forge logo]

From Sheet Metal To Large Sand Castings

Our Capacity and Rapid Quenching drop bottom ovens deliver precise processing.
We also serve the leading names in aerospace, automotive and advanced engineering.

Visit www.brindleforge-example.co.uk/ or call us Tel: +44 (0)1632 960318

[Put the crafted across the shires logo here, also include the text member somewhere close]

check on their website for other ideas that can help you with this project.

Target Market(s)

will be used at a trade show

Requirements
Nice to have
• modern design for UK manufacturing business

```html
<!DOCTYPE html>
<html lang="en">
<head>
<meta charset="utf-8">
<title>Brindle Forge Services – Exhibition Banner</title>
<link rel="stylesheet" href="https://fonts.googleapis.com/css2?family=Lato:wght@400;700;900&display=swap">
<style>
  :root {
    --brand-red: #d4262f;
    --deep-red: #a8161e;
    --ink-grey: #555a60;
    --soft-grey: #8b9096;
    --stage: #e6e7e9;
    --paper: #ffffff;
    --photo-light: #c9ccd0;
    --photo-dark: #6f747b;
  }
  * { box-sizing: border-box; margin: 0; padding: 0; }
  html, body {
    width: 855px; height: 1200px; overflow: hidden;
    background: var(--stage);
    font-family: "Lato", Arial, sans-serif;
  }
  .banner {
    position: absolute; left: 187px; top: 0;
    width: 480px; height: 1200px;
    background: var(--paper);
    overflow: hidden;
  }
  .brand {
    position: absolute; top: 38px; right: 40px;
    display: flex; align-items: center; gap: 10px;
  }
  .brand-square { width: 26px; height: 26px; background: var(--brand-red); }
  .brand-name {
    font-weight: 700; font-size: 17px; color: var(--ink-grey);
    letter-spacing: 0.3px;
  }
  .headline {
    position: absolute; top: 118px; left: 0; width: 100%;
    text-align: center; color: var(--brand-red);
    font-weight: 700; font-size: 39px; line-height: 1.2;
    text-transform: uppercase; letter-spacing: 0.5px;
  }
  .photo {
    position: absolute; top: 300px; left: 30px;
    width: 420px; height: 390px;
    background: linear-gradient(160deg, var(--photo-light) 0%, #a9adb2 55%, var(--photo-dark) 100%);
  }
  .chevron {
    position: absolute; top: 580px; left: 0; width: 480px; height: 200px;
  }
  .body-copy {
    position: absolute; top: 800px; left: 70px; width: 340px;
    text-align: center; color: var(--soft-grey);
    font-size: 15px; line-height: 1.5;
  }
  .body-copy p + p { margin-top: 18px; }
  .contact-band {
    position: absolute; top: 1010px; left: 0; width: 100%; height: 120px;
    background: var(--brand-red);
    display: flex; flex-direction: column; justify-content: center; align-items: center;
    gap: 8px; color: var(--paper);
    font-size: 17px; letter-spacing: 2px;
  }
  .base-strip {
    position: absolute; top: 1130px; left: 0; width: 100%; height: 70px;
    background: linear-gradient(180deg, #f1f1f2, #d9dadd);
  }
</style>
</head>
<body>
  <main class="banner">
    <div class="brand">
      <span class="brand-square"></span>
      <span class="brand-name">Brindle Forge Services</span>
    </div>

    <h1 class="headline">From Sheet Metal<br>to Large Sand<br>Castings</h1>

    <div class="photo" role="img" aria-label="Photograph of a company representative in a white shirt and red tie standing in a metal processing workshop"></div>

    <svg class="chevron" viewBox="0 0 480 200" aria-hidden="true">
      <polygon points="0,20 240,110 480,20 480,70 240,160 0,70" fill="var(--deep-red)"/>
      <polygon points="0,45 240,135 480,45 480,90 240,180 0,90" fill="var(--brand-red)"/>
      <polygon points="0,90 240,180 480,90 480,200 0,200" fill="var(--paper)"/>
    </svg>

    <section class="body-copy">
      <p>Our Capacity and Rapid Quenching drop bottom ovens deliver precise processing.</p>
      <p>We also serve the leading names in aerospace, automotive and advanced engineering.</p>
    </section>

    <footer class="contact-band">
      <span class="web">www.brindleforge-example.co.uk</span>
      <span class="phone">+44 (0)1632 960318</span>
    </footer>
    <div class="base-strip"></div>
  </main>
</body>
</html>
```